Brightwell is a company offering Colon Hydrotherapy (or colonics)

Brightwell offers Colon Hydrotherapy using an innovative FDA approved system from the USA. The system is called the TORVA system. The clinic is based in Whangarei, Northland and is the first business of this kind for Northland.
I used to use a design from the Prontaleaf website - a water symbol. However, I want a design that will convey freshness. I want something new and clean which conveys vitality and revitalisation .... perhaps water or bubbles but which brings across the idea of detoxing (which is what colon hydrotherapy does)
The clinic will only be completed in April so for now I have put my mobile number but once in the clinic this will need to be changed to a landline number ... the email address will also change. Thanks for any ideas you give me,
Updates

Hi. I need the name Brightwell first and foremost as this is the name of the Company Underneath this it has to say Colon Hydrotherapy to let people know what Brightwell is My name underneath that would be Marian Holcombe And all contact details to follow this. Thanks !

Target Market(s)

People who are wanting to "detox" and focusing on their health and wellbeing

Industry/Entity Type

Clinic

Contact Information for Business Card

Brightwell
Colon Hydrotherapy
Marian Holcombe
Unit B, 42c Ferrand Lane, Whangarei

021 0487 3916
brightwellclinic@mailnest.example

Font styles to use
Serif

Colors
cee9f6
33a6d7
86cae6

Requirements
Must have
• Stand out with colour or logo

```html
<!DOCTYPE html>
<html lang="en">
<head>
<meta charset="utf-8">
<title>Brightwell – Business Card</title>
<link href="https://fonts.googleapis.com/css2?family=Lora:wght@400;700&display=swap" rel="stylesheet">
<style>
  :root {
    --backdrop: #161616;
    --card-white: #f4f4f4;
    --brand-blue: #05a3c6;
    --gradient-top: #46c1dd;
    --gradient-bottom: #1a7ea6;
    --ink: #444444;
    --ink-strong: #3a3a3a;
    --logo-white: #ffffff;
  }
  * { box-sizing: border-box; margin: 0; padding: 0; }
  html, body {
    width: 1200px;
    height: 1000px;
    overflow: hidden;
    background: var(--backdrop);
    font-family: "Lora", serif;
  }
  .stage {
    position: relative;
    width: 1200px;
    height: 1000px;
  }
  .card {
    position: absolute;
    width: 630px;
    height: 360px;
    overflow: hidden;
    box-shadow: 0 18px 40px rgba(0,0,0,0.6);
  }
  /* Back of card: brand side */
  .card-back {
    left: 470px;
    top: 150px;
    background: linear-gradient(170deg, var(--gradient-top) 0%, var(--gradient-bottom) 100%);
    display: flex;
    align-items: center;
    justify-content: center;
  }
  .brand-lockup {
    display: flex;
    align-items: center;
    gap: 18px;
    color: var(--logo-white);
  }
  .brand-dot {
    width: 74px;
    height: 74px;
    border-radius: 50%;
    background: var(--logo-white);
  }
  .brand-words {
    display: flex;
    flex-direction: column;
    font-weight: 400;
    line-height: 1;
  }
  .brand-name {
    font-size: 72px;
    letter-spacing: 4px;
  }
  .brand-sub {
    font-size: 20px;
    letter-spacing: 20px;
    margin-top: 6px;
  }
  /* Front of card: contact side */
  .card-front {
    left: 110px;
    top: 470px;
    background: linear-gradient(180deg, #ffffff 0%, var(--card-white) 60%, #e6e6e6 100%);
  }
  .accent-circle {
    position: absolute;
    left: 0;
    top: 0;
  }
  .contact {
    position: absolute;
    left: 318px;
    top: 118px;
    color: var(--ink);
    white-space: nowrap;
  }
  .company-name {
    font-size: 24px;
    font-weight: 700;
    color: var(--brand-blue);
    line-height: 1.2;
  }
  .company-service {
    font-size: 13px;
    letter-spacing: 2px;
    text-transform: uppercase;
    color: var(--ink);
    margin-top: 2px;
    margin-bottom: 14px;
  }
  .contact-name {
    font-size: 19px;
    font-weight: 700;
    color: var(--ink-strong);
    margin-bottom: 10px;
  }
  .contact-address,
  .contact-line {
    font-size: 14.5px;
    line-height: 1.4;
  }
  .contact-address { margin-bottom: 6px; }
  .contact-line + .contact-line { margin-top: 4px; }
</style>
</head>
<body>
<main class="stage">
  <section class="card card-back" aria-label="Card back">
    <div class="brand-lockup">
      <span class="brand-dot" aria-hidden="true"></span>
      <div class="brand-words">
        <span class="brand-name">TORVA</span>
        <span class="brand-sub">SYSTEM</span>
      </div>
    </div>
  </section>

  <section class="card card-front" aria-label="Card front">
    <svg class="accent-circle" width="300" height="270" viewBox="0 0 300 270" aria-hidden="true">
      <circle cx="100" cy="40" r="200" fill="var(--brand-blue)"/>
    </svg>
    <div class="contact">
      <p class="company-name">Brightwell</p>
      <p class="company-service">Colon Hydrotherapy</p>
      <p class="contact-name">Marian Holcombe</p>
      <p class="contact-address">Unit B<br>42c Ferrand Lane, Whangarei</p>
      <p class="contact-line">p : 021 0487 3916</p>
      <p class="contact-line">e : brightwellclinic@mailnest.example</p>
    </div>
  </section>
</main>
</body>
</html>
```